Jolly Paws Business Card Update

I have a business card which I love. I want to keep the same logo, colours, font and style. I want to upgrade the scripting and remove some elements and add others.
On the front side under Services - remove the existing wording and insert - Providing individual coaching strategies to create happy, healthy and social canine companions
Under Rebecca Thornley amend the current wording to read: Qualified in Dog Behavioural Training, Natural Animal Healthcare and Animal Health Science
On the reverse side to remove the web address.

```html
<!DOCTYPE html>
<html lang="en">
<head>
<meta charset="utf-8">
<title>Jolly Paws Business Card</title>
<link rel="stylesheet" href="https://fonts.googleapis.com/css2?family=Dosis:wght@500&family=Dancing+Script:wght@500&family=Roboto+Condensed:wght@400&display=swap">
<style>
  :root {
    --backdrop: #363a42;
    --sky-light: #22a6e6;
    --sky-mid: #1676cc;
    --sky-deep: #1a48a8;
    --ribbon-light: #d42a2c;
    --ribbon-deep: #7e1414;
    --cream: #f2efe2;
    --cream-text: #f7f1e0;
    --wine: #8a1e22;
    --scarlet: #d3242b;
    --white: #ffffff;
  }
  html, body {
    margin: 0;
    padding: 0;
    width: 1200px;
    height: 1177px;
    overflow: hidden;
    background: var(--backdrop);
  }
  .canvas {
    position: relative;
    width: 1200px;
    height: 1177px;
  }
  .card {
    position: absolute;
    left: 283px;
    width: 669px;
    height: 411px;
    filter: drop-shadow(0 4px 6px rgba(0,0,0,0.45));
  }
  .card svg { display: block; width: 100%; height: 100%; }
  .card--front { top: 150px; }
  .card--back { top: 624px; }
  .brand-name { font-family: "Dosis", sans-serif; font-weight: 500; fill: var(--white); letter-spacing: 2px; }
  .brand-name--badge { fill: var(--sky-deep); letter-spacing: 0.5px; }
  .script { font-family: "Dancing Script", cursive; font-weight: 500; }
  .tagline { fill: var(--cream-text); }
  .section-title { fill: var(--white); }
  .service-item, .credential, .contact-text { font-family: "Roboto Condensed", sans-serif; }
  .service-item { fill: var(--white); }
  .mission { fill: var(--wine); }
  .mission-highlight { fill: var(--scarlet); }
  .holder-name { fill: var(--cream-text); }
  .credential, .contact-text { fill: var(--cream-text); }
</style>
</head>
<body>
<main class="canvas">

  <!-- Front side -->
  <section class="card card--front" aria-label="Card front">
    <svg viewBox="0 0 557 342" xmlns="http://www.w3.org/2000/svg">
      <defs>
        <radialGradient id="frontSky" cx="0.5" cy="0.05" r="0.9">
          <stop offset="0" stop-color="var(--sky-light)"/>
          <stop offset="0.6" stop-color="var(--sky-mid)"/>
          <stop offset="1" stop-color="var(--sky-deep)"/>
        </radialGradient>
        <linearGradient id="ribbon" x1="0" y1="0" x2="1" y2="0">
          <stop offset="0" stop-color="var(--ribbon-deep)"/>
          <stop offset="0.5" stop-color="var(--ribbon-light)"/>
          <stop offset="1" stop-color="var(--ribbon-deep)"/>
        </linearGradient>
      </defs>
      <rect class="front-sky" width="557" height="342" fill="url(#frontSky)"/>
      <circle class="brand-mark" cx="278" cy="88" r="72" fill="var(--cream)"/>
      <text class="brand-name" x="278" y="218" font-size="44" text-anchor="middle">JOLLY PAWS</text>
      <path class="front-ribbon" d="M0 290 Q278 240 557 298 L557 342 L0 342 Z" fill="url(#ribbon)"/>
      <text class="script tagline" x="278" y="320" font-size="24" text-anchor="middle">Happy Dogs, Happy Owners</text>
    </svg>
  </section>

  <!-- Back side -->
  <section class="card card--back" aria-label="Card back">
    <svg viewBox="0 0 557 342" xmlns="http://www.w3.org/2000/svg">
      <defs>
        <linearGradient id="backSky" x1="0" y1="0" x2="1" y2="0.4">
          <stop offset="0" stop-color="var(--sky-deep)"/>
          <stop offset="0.6" stop-color="var(--sky-mid)"/>
          <stop offset="1" stop-color="var(--sky-light)"/>
        </linearGradient>
        <linearGradient id="ribbonBack" x1="0" y1="0" x2="1" y2="0">
          <stop offset="0" stop-color="var(--ribbon-deep)"/>
          <stop offset="0.5" stop-color="var(--ribbon-light)"/>
          <stop offset="1" stop-color="var(--ribbon-deep)"/>
        </linearGradient>
      </defs>
      <rect class="back-cream" width="557" height="342" fill="var(--cream)"/>
      <path class="back-sky" d="M0 0 L557 0 L557 122 Q380 150 230 165 Q110 170 0 125 Z" fill="url(#backSky)"/>
      <path class="back-sky-stripe" d="M310 0 Q230 60 130 100 Q230 70 330 0 Z" fill="var(--sky-light)" opacity="0.55"/>
      <circle class="brand-mark" cx="64" cy="68" r="63" fill="var(--cream)"/>
      <text class="brand-name brand-name--badge" x="64" y="75" font-size="19" text-anchor="middle">Jolly Paws</text>
      <text class="script section-title" x="156" y="34" font-size="21">Services</text>
      <g class="service-list" font-size="14.5">
        <text class="service-item" x="245" y="75">•Behavioral Consults, Training</text>
        <text class="service-item" x="245" y="95">•Complex Skills &amp; Walking Coaching</text>
        <text class="service-item" x="245" y="116">•Diet &amp; Nutrition, Massage</text>
        <text class="service-item" x="245" y="137">•Natural Healthcare Options</text>
      </g>
      <text class="script mission" x="278" y="196" font-size="19" text-anchor="middle">Providing individual coaching strategies to create</text>
      <text class="script mission" x="278" y="219" font-size="19" text-anchor="middle"><tspan class="mission-highlight">happy, healthy &amp; social</tspan> canine companions</text>
      <path class="back-ribbon" d="M0 258 Q278 222 557 262 L557 342 L0 342 Z" fill="url(#ribbonBack)"/>
      <text class="script holder-name" x="50" y="290" font-size="21">Rebecca Thornley</text>
      <text class="credential" x="50" y="310" font-size="13.5">Qualified in Dog Behavioural Training, Natural</text>
      <text class="credential" x="50" y="330" font-size="13.5">Animal Healthcare &amp; Animal Health Science</text>
      <line class="contact-divider" x1="333" y1="296" x2="333" y2="333" stroke="var(--cream-text)" stroke-width="1"/>
      <g class="contact-icon contact-icon--phone">
        <circle cx="349" cy="305" r="6" fill="var(--cream-text)"/>
        <rect x="346.5" y="301" width="5" height="8" rx="1" fill="var(--ribbon-deep)"/>
      </g>
      <text class="contact-text" x="362" y="310" font-size="14">0400 726 158</text>
      <g class="contact-icon contact-icon--mail">
        <circle cx="349" cy="326" r="6" fill="var(--cream-text)"/>
        <rect x="345.5" y="323.5" width="7" height="5" fill="var(--ribbon-deep)"/>
      </g>
      <text class="contact-text" x="362" y="331" font-size="14">jollypaws.cards@mail.com</text>
    </svg>
  </section>

</main>
</body>
</html>
```